Coffee Package Design

We need a new package design for a coffee company. Need to be a mix between modern and classic design combined together. We are open to different ideas.
We changing our product name from Café Verlano to Café Brisota. The picture upload
shows what the product looks like. We want something completely different. The name of the company should go on the back of the package.
Updates

Hello Everyone,

Please read description, we are going with a new name and design for the product.

Café Brisota. Café Verlano is what we are replacing with Café Brisota, we are looking for new

look and design, please submit new designs.

There is a change in the description. Please take out Premium coffee blend and replace with Italian Roast.                                    

Industry/Entity Type

Cafe

Requirements
Must have
• You can use up to 6 colors.
Please put these items on design: Café Brisota (this is the product name), Regular Premium Blend Coffee, 100% Arabica,
Dulmore & Sons (name of the company), Tyler, TX on the back of the package

The file uploaded is an example of one of our products and how the package film
is sized.

```html
<!DOCTYPE html>
<html lang="en">
<head>
<meta charset="utf-8">
<title>Café Brisota – Package Label Colourways</title>
<link rel="stylesheet" href="https://fonts.googleapis.com/css2?family=Arimo:wght@400;700&display=swap">
<style>
  :root {
    --page: #ffffff;
    --frame: #050505;
    --label-green: #4f7a4f;
    --label-dark: #161616;
    --name-ink: #ffffff;
    --origin-ink: #9a9a9a;
    --blend-ink: #c7ad6a;

    --stone: #a39f89;
    --slate: #5a5a5a;
    --amber: #9c6617;
    --night: #2a2a2a;
  }

  html, body {
    margin: 0;
    width: 1200px;
    height: 1200px;
    overflow: hidden;
    background: var(--page);
    font-family: "Arimo", Arial, sans-serif;
  }

  .board {
    position: relative;
    width: 1200px;
    height: 1200px;
  }

  .label {
    position: absolute;
    width: 326px;
    height: 410px;
    box-sizing: border-box;
    border: 10px solid var(--frame);
    background: var(--frame);
    box-shadow: 4px 6px 10px rgba(0, 0, 0, 0.35);
    overflow: hidden;
  }

  .label--stone { left: 247px; top: 190px; --tone: var(--stone); }
  .label--slate { left: 600px; top: 190px; --tone: var(--slate); }
  .label--amber { left: 247px; top: 626px; --tone: var(--amber); }
  .label--night { left: 600px; top: 630px; --tone: var(--night); }

  .label-art {
    position: absolute;
    inset: 0;
    background:
      linear-gradient(160deg,
        var(--tone) 0%,
        var(--label-green) 45%,
        var(--label-dark) 78%,
        var(--label-dark) 100%);
  }

  .product-name {
    position: absolute;
    left: 0;
    right: 0;
    top: 150px;
    margin: 0;
    text-align: center;
    color: var(--name-ink);
    font-weight: 700;
    font-size: 50px;
    line-height: 52px;
  }

  .product-details {
    position: absolute;
    left: 0;
    right: 0;
    top: 322px;
    margin: 0;
    text-align: center;
    font-size: 15px;
    line-height: 24px;
  }
  .origin { display: block; color: var(--origin-ink); }
  .blend { display: block; color: var(--blend-ink); }
</style>
</head>
<body>
<main class="board">

  <article class="label label--stone">
    <div class="label-art" role="img" aria-label="Decorative label artwork in stone, green and black tones"></div>
    <h2 class="product-name">Café<br>Brisota</h2>
    <p class="product-details"><span class="origin">100% Arabica</span><span class="blend">REGULAR</span></p>
  </article>

  <article class="label label--slate">
    <div class="label-art" role="img" aria-label="Decorative label artwork in slate grey, green and black tones"></div>
    <h2 class="product-name">Café<br>Brisota</h2>
    <p class="product-details"><span class="origin">100% Arabica</span><span class="blend">REGULAR</span></p>
  </article>

  <article class="label label--amber">
    <div class="label-art" role="img" aria-label="Decorative label artwork in amber, green and black tones"></div>
    <h2 class="product-name">Café<br>Brisota</h2>
    <p class="product-details"><span class="origin">100% Arabica</span><span class="blend">REGULAR</span></p>
  </article>

  <article class="label label--night">
    <div class="label-art" role="img" aria-label="Decorative label artwork in charcoal, green and black tones"></div>
    <h2 class="product-name">Café<br>Brisota</h2>
    <p class="product-details"><span class="origin">100% Arabica</span><span class="blend">REGULAR</span></p>
  </article>

</main>
</body>
</html>
```